Minnesota Firefighter Training

I am looking at initial advertisement to provide firefighter training in the State of Minnesota. Training will include Firefighter I, Firefighter II, Driver/Operator-Pumper, First Aid, CPR, Fire Instructor I, along with Firefighter continuing education. I have attached company logo and some pictures that I have taken during my training sessions. If you find others that you may like please use generic ones with no fire department logos or identification in them. Please let me know if you have other questions at kellan@harborvalepro.com . Web address to be included is www.harborvalepro.com ALso please include return address on mailing portion as follows: Harborvale Skills Group, LLC PO Box 841 Ralston, IA 50944 (515) 555-0148.

```html
<!DOCTYPE html>
<html lang="en">
<head>
<meta charset="utf-8">
<title>Harborvale Skills Group – Firefighter Training</title>
<link href="https://fonts.googleapis.com/css2?family=Roboto+Slab:wght@700;900&display=swap" rel="stylesheet">
<style>
  :root {
    --bg-dark: #151515;
    --bg-mid: #2e2e2e;
    --yellow: #f4e81a;
    --white: #ffffff;
    --muted: #bdbdbd;
    --brand-red: #b8261e;
  }
  * { margin: 0; padding: 0; box-sizing: border-box; }
  html, body { width: 1200px; height: 932px; overflow: hidden; background: var(--bg-dark); }
  .ad {
    position: relative;
    width: 1200px;
    height: 932px;
    background:
      repeating-linear-gradient(45deg, rgba(255,255,255,0.025) 0 6px, rgba(0,0,0,0.04) 6px 12px),
      radial-gradient(ellipse at 50% 45%, var(--bg-mid) 0%, var(--bg-dark) 80%);
    font-family: "Roboto Slab", Georgia, serif;
    font-weight: 900;
    color: var(--white);
  }
  .brand {
    position: absolute;
    left: 70px; top: 40px;
    width: 250px;
    display: flex; flex-direction: column; align-items: center; gap: 12px;
  }
  .brand-mark {
    width: 150px; height: 150px; border-radius: 50%;
    background: var(--brand-red);
  }
  .brand-name {
    font-size: 26px; line-height: 1.15; text-align: center; color: var(--white);
  }
  .headline {
    position: absolute;
    left: 350px; top: 78px; width: 800px;
    color: var(--yellow);
    font-size: 42px; line-height: 1.3;
    font-weight: 900;
    text-align: center;
    letter-spacing: 1px;
  }
  .photo { position: absolute; }
  .photo-hose { left: 0; top: 307px; width: 387px; height: 238px;
    background:
      radial-gradient(ellipse at 25% 55%, #e7e6e1 0%, rgba(231,230,225,0) 55%),
      radial-gradient(ellipse at 80% 85%, #b98a2c 0%, rgba(185,138,44,0) 45%),
      linear-gradient(135deg, #bfc1bd 0%, #8d8b86 55%, #4f4a44 100%); }
  .photo-crew { left: 402px; top: 307px; width: 396px; height: 238px;
    background:
      radial-gradient(ellipse at 20% 35%, #ffd27a 0%, rgba(255,210,122,0) 40%),
      radial-gradient(ellipse at 75% 70%, #26282b 0%, rgba(38,40,43,0) 55%),
      linear-gradient(120deg, #f0a23a 0%, #d4641e 45%, #4a3a2c 80%, #1f1f1f 100%); }
  .photo-line { left: 402px; top: 557px; width: 396px; height: 233px;
    background:
      radial-gradient(ellipse at 15% 20%, #ffb95a 0%, rgba(255,185,90,0) 40%),
      radial-gradient(ellipse at 55% 70%, #e9b84a 0%, rgba(233,184,74,0) 40%),
      linear-gradient(160deg, #c8612a 0%, #8c5a34 45%, #3e3a36 75%, #c9c2b4 100%); }
  .photo-attack { left: 816px; top: 557px; width: 384px; height: 233px;
    background:
      radial-gradient(ellipse at 25% 30%, #ffc773 0%, rgba(255,199,115,0) 45%),
      radial-gradient(ellipse at 80% 80%, #e6e1d6 0%, rgba(230,225,214,0) 40%),
      linear-gradient(110deg, #f0a84e 0%, #d2602a 40%, #38332e 75%, #6f6a63 100%); }
  .courses {
    position: absolute; left: 826px; top: 352px;
    list-style: none;
    font-weight: 700;
    font-size: 27px; line-height: 1.3; color: var(--yellow);
  }
  .availability {
    position: absolute; left: 10px; top: 588px; width: 375px;
    color: var(--yellow); font-size: 40px; line-height: 1.22; text-align: center;
  }
  .contact {
    position: absolute; left: 72px; top: 830px; width: 1080px;
    display: flex; justify-content: space-between;
    font-size: 42px; line-height: 1; color: var(--white);
  }
  .return-address {
    position: absolute; left: 0; top: 896px; width: 1200px;
    text-align: center;
    font-weight: 700; font-size: 17px; color: var(--muted);
    letter-spacing: 0.5px;
  }
</style>
</head>
<body>
<main class="ad">
  <div class="brand">
    <div class="brand-mark"></div>
    <div class="brand-name">Harborvale Skills Group</div>
  </div>

  <h1 class="headline">EVERYONE IS CREATED EQUAL....<br>THEN A FEW BECOME<br>FIREFIGHTERS</h1>

  <div class="photo photo-hose" role="img" aria-label="Firefighter in protective gear spraying a hose line through smoke"></div>
  <div class="photo photo-crew" role="img" aria-label="Firefighters with air packs watching a large training fire"></div>
  <div class="photo photo-line" role="img" aria-label="Firefighter crew advancing a hose line toward flames"></div>
  <div class="photo photo-attack" role="img" aria-label="Firefighters attacking a burning structure with water"></div>

  <ul class="courses">
    <li>Firefighter I / II</li>
    <li>Hazmat Operations</li>
    <li>Driver/Operator</li>
    <li>First Aid, CPR, EMS</li>
    <li>Fire Instructor I</li>
  </ul>

  <p class="availability">Now<br>Available<br>in Minnesota.</p>

  <p class="contact">
    <span class="contact-web">www.harborvalepro.com</span>
    <span class="contact-phone">(515) 555-0148</span>
  </p>

  <address class="return-address">Harborvale Skills Group, LLC &nbsp;·&nbsp; PO Box 841 &nbsp;·&nbsp; Ralston, IA 50944</address>
</main>
</body>
</html>
```